Corvane Supplies Business Card

Professional business card that stand out to our potential customers. Front and back with clean modern design

Industry/Entity Type

Oil and gas

Contact Information for Business Card

Name, address, website , office phone and cell number

Requirements
Must have
• Editable files for each employee

```html
<!DOCTYPE html>
<html lang="en">
<head>
<meta charset="utf-8">
<title>Corvane Supplies Business Card</title>
<link rel="stylesheet" href="https://fonts.googleapis.com/css2?family=Arimo:wght@400;700&display=swap">
<style>
  :root {
    --backdrop: #3d3d3d;
    --card-dark: #2f2f2f;
    --card-light: #ffffff;
    --edge-cyan: #19a9cf;
    --brand-red: #ee1c1c;
    --brand-cyan: #1fb1d4;
    --text-light: #f2f2f2;
  }
  * { margin: 0; padding: 0; box-sizing: border-box; }
  html, body {
    width: 1200px; height: 803px; overflow: hidden;
    background: var(--backdrop);
    font-family: "Arimo", Arial, sans-serif;
  }
  .canvas {
    width: 1200px; height: 803px;
    display: flex; align-items: center; justify-content: center; gap: 48px;
  }
  .card {
    width: 520px; height: 300px;
    border-radius: 22px;
    position: relative;
    box-shadow: 0 4px 0 var(--edge-cyan);
  }
  .card--front { background: var(--card-dark); }
  .card--back {
    background: var(--card-light);
    display: flex; flex-direction: column; align-items: center; justify-content: center; gap: 14px;
  }
  .brand {
    display: flex; align-items: center; gap: 10px;
    font-weight: 700; text-transform: uppercase; letter-spacing: 1px;
    color: var(--brand-red);
  }
  .brand__square { width: 16px; height: 16px; background: var(--brand-cyan); }
  .card--front .brand { position: absolute; left: 40px; top: 48px; font-size: 20px; }
  .card--back .brand { font-size: 32px; }
  .brand__square--large { width: 28px; height: 28px; }
  .contact { position: absolute; left: 40px; top: 104px; color: var(--text-light); }
  .contact__name { font-size: 24px; font-weight: 700; color: var(--brand-red); }
  .contact__title { font-size: 13px; color: var(--brand-cyan); margin-bottom: 14px; }
  .contact__address { font-size: 13px; line-height: 1.35; margin-bottom: 10px; }
  .contact__list { list-style: none; font-size: 13px; line-height: 1.55; }
  .contact__list li { display: flex; align-items: center; gap: 8px; }
  .contact__icon { width: 12px; height: 12px; fill: none; stroke: var(--brand-red); stroke-width: 2; }
</style>
</head>
<body>
<main class="canvas">
  <section class="card card--front" aria-label="Business card front">
    <div class="brand"><span class="brand__square"></span>Corvane Supplies</div>
    <div class="contact">
      <p class="contact__name">Dale Morrow</p>
      <p class="contact__title">President</p>
      <p class="contact__address">4120 Birchwood Road<br>Halden, Canada 20418</p>
      <ul class="contact__list">
        <li><svg class="contact__icon" viewBox="0 0 12 12"><path d="M2 1l2 0 1 3-1.5 1a6 6 0 0 0 3.5 3.5L8 7l3 1v2l-1 1C5 11 1 7 1 2z"/></svg>555-210-4471</li>
        <li><svg class="contact__icon" viewBox="0 0 12 12"><rect x="3" y="1" width="6" height="10" rx="1"/></svg>555-210-8832</li>
        <li><svg class="contact__icon" viewBox="0 0 12 12"><rect x="1" y="2.5" width="10" height="7"/><path d="M1 2.5l5 4 5-4"/></svg>info@corvanesupplies.com</li>
        <li><svg class="contact__icon" viewBox="0 0 12 12"><circle cx="6" cy="6" r="5"/><path d="M1 6h10M6 1c-3 3-3 7 0 10M6 1c3 3 3 7 0 10"/></svg>www.corvanesupplies.com</li>
      </ul>
    </div>
  </section>
  <section class="card card--back" aria-label="Business card back">
    <div class="brand"><span class="brand__square brand__square--large"></span>Corvane Supplies</div>
  </section>
</main>
</body>
</html>
```